Stationery Design Project - KLVA Partners

Business Cards
Size: 90mm x 55mm
Letterhead
Size: A4 - 210mm x 297mm
With Compliments Slip
Size: DL - 210mm x 99mm
Presentation Folder
Size: A4

KLVA Partners
website: www.klvapartners.com.au (Under construction)
Offices: *Perth *Brisbane * Seoul

A company that supply Safety consultantcy services

Industry/Entity Type

Business

```html
<!DOCTYPE html>
<html lang="en">
<head>
<meta charset="utf-8">
<title>KLVA Partners – Business Card</title>
<link rel="stylesheet" href="https://fonts.googleapis.com/css2?family=Montserrat:wght@400;500;600&display=swap">
<style>
  :root {
    --page-bg: #e9eaec;
    --card-white: #ffffff;
    --card-grey: #dfe2e4;
    --brand-blue: #1d5f8c;
    --ink: #2b2b2b;
    --mark-blue: #4fb3e6;
    --deco-light: #f4f6f7;
    --deco-mid: #cfd6da;
    --deco-blue: #a9dcf2;
  }
  * { margin: 0; padding: 0; box-sizing: border-box; }
  html, body { width: 1200px; height: 900px; overflow: hidden; }
  body {
    background: var(--page-bg);
    font-family: "Montserrat", sans-serif;
    position: relative;
  }
  .card {
    position: absolute;
    top: 293px;
    width: 513px;
    height: 313px;
    border-radius: 24px;
    overflow: hidden;
    background: radial-gradient(ellipse at 30% 20%, var(--card-white) 0%, var(--card-white) 40%, var(--card-grey) 100%);
    box-shadow: 0 4px 14px rgba(0,0,0,0.18);
  }
  .card--front { left: 73px; }
  .card--back { left: 616px; }

  .cube-decoration {
    position: absolute;
    border-radius: 6px;
    background: linear-gradient(160deg, var(--deco-light) 0%, var(--deco-blue) 50%, var(--deco-mid) 100%);
    opacity: 0.85;
  }
  .card--front .cube-decoration { left: 392px; top: 48px; width: 140px; height: 270px; }
  .card--back .cube-decoration { left: 308px; top: 92px; width: 210px; height: 222px; }

  .brand {
    position: absolute;
    display: flex;
    align-items: center;
    gap: 14px;
  }
  .brand__square {
    width: 46px; height: 46px;
    background: var(--mark-blue);
  }
  .brand__name {
    font-size: 27px;
    font-weight: 500;
    color: var(--brand-blue);
    letter-spacing: 1px;
    text-transform: lowercase;
  }
  .card--front .brand { left: 32px; top: 130px; }
  .card--back .brand { left: 34px; top: 44px; }

  .web-line {
    position: absolute;
    left: 172px;
    top: 278px;
    font-size: 10px;
    font-weight: 600;
    letter-spacing: 1.4px;
    color: var(--brand-blue);
  }

  .person { position: absolute; left: 46px; top: 172px; }
  .person__name {
    font-size: 18px;
    font-weight: 600;
    letter-spacing: 2px;
    color: var(--brand-blue);
    font-variant: small-caps;
  }
  .person__role {
    font-size: 11px;
    font-weight: 500;
    letter-spacing: 1.6px;
    color: var(--ink);
    text-transform: uppercase;
    margin-top: 2px;
  }

  .contact { position: absolute; left: 0; top: 236px; list-style: none; }
  .contact__row {
    display: flex;
    align-items: flex-end;
    height: 13px;
    font-size: 10px;
    letter-spacing: 1.2px;
    color: var(--ink);
    font-variant: small-caps;
  }
  .contact__label {
    width: 42px;
    text-align: right;
    padding-right: 3px;
    color: var(--brand-blue);
    border-bottom: 1px solid var(--brand-blue);
    border-right: 1px solid var(--brand-blue);
    line-height: 11px;
  }
  .contact__label--blank { border: none; }
  .contact__value { padding-left: 4px; line-height: 11px; }
</style>
</head>
<body>

  <section class="card card--front" aria-label="Business card front">
    <div class="cube-decoration" role="img" aria-label="Large decorative brand symbol area"></div>
    <div class="brand">
      <span class="brand__square"></span>
      <span class="brand__name">KLVA Partners</span>
    </div>
    <p class="web-line">WWW.KLVAPARTNERS.COM.AU</p>
  </section>

  <section class="card card--back" aria-label="Business card back">
    <div class="cube-decoration" role="img" aria-label="Large decorative brand symbol area"></div>
    <div class="brand">
      <span class="brand__square"></span>
      <span class="brand__name">KLVA Partners</span>
    </div>
    <div class="person">
      <p class="person__name">Daniel Morrow</p>
      <p class="person__role">Managing Director</p>
    </div>
    <ul class="contact">
      <li class="contact__row"><span class="contact__label">A</span><span class="contact__value">48 Harbour Lane</span></li>
      <li class="contact__row"><span class="contact__label contact__label--blank"></span><span class="contact__value">Perth, WA 6000</span></li>
      <li class="contact__row"><span class="contact__label">P</span><span class="contact__value">08 9000 4127</span></li>
      <li class="contact__row"><span class="contact__label">E</span><span class="contact__value">info@klvapartners.com.au</span></li>
      <li class="contact__row"><span class="contact__label">W</span><span class="contact__value">www.klvapartners.com.au</span></li>
    </ul>
  </section>

</body>
</html>
```